Brackley Yard Services Flyer Design

I need a new flyer design for my business, Brackley Yard Services. I’ll be providing my old flyer and logo as references. The new flyer should feature updated wording, contact information, logos, and photos, but still keep the original “What We Do” section and include the phrase “Don’t See? Just Ask!” somewhere near the services. The flyer needs to look great in black and white for door-to-door handouts but also be eye-catching and professional enough for social media use.

The updated content should include the headline “Transforming Outdoor Spaces with Hard Work & Precision” and highlight three main service areas: Landscaping Services (project-based landscaping to clean, prepare, and transform outdoor spaces with precision), Property Cleanup (quick hauls, debris removal, or full cleanouts—no job too big or small), and Ground Preparation (pad preparation, brush removal, and fire lines—making properties safe, functional, and project-ready).

Please also include a “Why Choose Us?” section that lists: Locally owned since 2022, Reliable & affordable – no corners cut, Professional results you can trust, LICENSED AND Insured, and Quality work / on time / references / flexible / follow-up.

At the bottom, include the contact details: Call or Text Today!
www.brackleyyard.example
| sales@brackleyyard.example
| (555) 019-4827

The overall design should be clean, professional, and easy to read with a layout that clearly shows what we offer. Use visuals that represent outdoor services, landscaping, and property cleanup/prep work. I want something that feels trustworthy, family-friendly, and modern.
Use the same photo of leaf clean up from the original flyer if possible.
Our company colors are also black and white. For the most part.

```html
<!DOCTYPE html>
<html lang="en">
<head>
<meta charset="utf-8">
<title>Brackley Yard Services Flyer</title>
<link rel="stylesheet" href="https://fonts.googleapis.com/css2?family=Francois+One&family=Syncopate:wght@700&family=Poppins:wght@400;500;600;700&display=swap">
<style>
:root{
  --backdrop:#8c8c8c;
  --ink:#0d0d0d;
  --paper:#ffffff;
  --panel-grey:#9a9a9a;
  --rule:#4a4a4a;
  --headline-font:"Francois One", sans-serif;
  --display-font:"Syncopate", sans-serif;
  --body-font:"Poppins", sans-serif;
}
*{box-sizing:border-box;margin:0;padding:0}
html,body{width:921px;height:1200px;overflow:hidden;background:var(--backdrop)}
.stage{position:relative;width:921px;height:1200px;background:var(--backdrop);overflow:hidden}
.flyer{position:absolute;left:101px;top:83px;width:1312px;height:1886px;background:var(--paper);transform:scale(0.5482);transform-origin:0 0;overflow:hidden;font-family:var(--body-font);color:var(--ink)}
.abs{position:absolute}

/* header */
.hero{left:0;top:0;width:1312px;height:530px;background:var(--ink)}
.hero-photo{left:700px;top:0;width:612px;height:530px;
  background:linear-gradient(90deg,var(--ink) 0%,rgba(13,13,13,0) 28%),
  radial-gradient(ellipse at 70% 85%,#a4582a 0%,rgba(164,88,42,0) 55%),
  linear-gradient(160deg,#3f4a1e 0%,#7f8a2c 35%,#8c6a3a 60%,#6b3a1c 100%)}
.brand{left:68px;top:70px;display:flex;align-items:center;gap:22px}
.brand-mark{width:70px;height:70px;background:var(--paper)}
.brand-name{font-family:var(--headline-font);font-size:46px;line-height:1.05;color:var(--paper);text-transform:uppercase;width:360px}
.headline{left:72px;top:214px;font-family:var(--headline-font);font-size:62px;line-height:77px;color:var(--paper);text-transform:uppercase;letter-spacing:1px}

/* service areas */
.section-title{font-family:var(--display-font);font-weight:700;font-size:40px;letter-spacing:1px;text-transform:uppercase;white-space:nowrap}
.areas-title{left:0;width:1312px;top:545px;text-align:center}
.area-photo{top:625px;width:377px;height:207px}
.area-photo.trim{border:2px solid var(--paper);outline:0}
.area-card{top:832px;width:357px;height:182px;border:2px solid var(--ink);border-top:0;border-bottom-right-radius:28px;text-align:center;padding:8px 10px 0}
.area-card h3{font-size:23px;font-weight:600;line-height:27px;text-transform:uppercase}
.area-card .dash{width:36px;height:2px;background:var(--ink);margin:9px auto 10px}
.area-card p{font-size:18.5px;line-height:24.5px}

/* ask banner */
.rule{height:2px;background:var(--rule)}
.slant-banner{clip-path:polygon(4% 0,100% 0,96% 100%,0 100%);background:var(--ink);color:var(--paper);font-family:var(--headline-font);text-transform:uppercase;text-align:center}

/* why choose us */
.why-title{left:64px;top:1143px}
.perk-icon{width:84px;height:73px;border:2px dashed var(--ink);border-radius:6px;display:flex;align-items:center;justify-content:center;background:var(--paper);box-shadow:3px 3px 0 var(--ink)}
.perk-label{width:260px;text-align:center;font-size:23.5px;font-weight:600;line-height:30px}
.perk-note{width:270px;text-align:center;font-size:17.5px;line-height:22px}
.perk-note.wide{font-size:20.5px;line-height:25px}

/* what we do panel */
.panel-back{left:630px;top:1129px;width:653px;height:721px;background:var(--panel-grey)}
.panel{left:656px;top:1146px;width:656px;height:740px;background:var(--ink);border-top-left-radius:100px;color:var(--paper)}
.panel-outline{left:630px;top:1129px;width:653px;height:721px;border:1.5px solid #777;border-left:0;border-top:0;border-bottom-right-radius:110px}
.panel-title{left:741px;top:1236px;color:var(--paper)}
.col-head{font-size:26px;font-weight:600;color:var(--paper);text-transform:uppercase}
.dot-rule{height:2px;background:var(--paper)}
.dot-rule::after{content:"";position:absolute;right:-3px;top:-3px;width:8px;height:8px;border-radius:50%;background:var(--paper)}
.task{display:flex;align-items:center;gap:14px;font-size:20.5px;color:var(--paper);white-space:nowrap;line-height:24px}
.task-icon{flex:none;width:31px;height:31px;border:1.5px solid var(--paper);border-radius:7px;display:flex;align-items:center;justify-content:center}

/* contact */
.contact{left:94px;display:flex;align-items:center;gap:12px;white-space:nowrap}
.contact-icon{width:30px;height:30px;border-radius:6px;background:var(--ink);display:flex;align-items:center;justify-content:center}
.contact-text{font-size:24px;font-weight:500}
.contact-text.phone{font-size:40px;font-weight:600}
</style>
</head>
<body>
<div class="stage">
<div class="flyer">

  <!-- header -->
  <div class="abs hero"></div>
  <div class="abs hero-photo" role="img" aria-label="Photo of a rake gathering autumn leaves on a lawn beside a burlap leaf bag"></div>
  <div class="abs brand">
    <div class="brand-mark"></div>
    <div class="brand-name">Brackley Yard Services</div>
  </div>
  <h1 class="abs headline">Transforming<br>Outdoor Spaces With<br>Hard Work &amp; Precision</h1>

  <!-- service areas -->
  <h2 class="abs section-title areas-title">Our Service Areas</h2>

  <div class="abs area-photo" style="left:65px;background:linear-gradient(180deg,#6d7b3c 0%,#5f8a2e 45%,#3f6b1e 75%,#9aa090 100%)" role="img" aria-label="Photo of a worker trimming a hedge with a power trimmer"></div>
  <div class="abs area-photo" style="left:483px;background:linear-gradient(160deg,#8aa0b8 0%,#5b5a52 40%,#7a7466 70%,#2f4c8c 100%)" role="img" aria-label="Photo of a dumpster filled with carpet, furniture and household debris"></div>
  <div class="abs area-photo" style="left:898px;background:linear-gradient(180deg,#b9bfc4 0%,#8c8a80 45%,#a89a82 70%,#807766 100%)" role="img" aria-label="Photo of a prepared gravel patio with pavers and a wooden fence"></div>

  <div class="abs area-card" style="left:77px">
    <h3>Landscaping<br>Services</h3>
    <div class="dash"></div>
    <p>Project-based landscaping to clean, prepare, and transform outdoor spaces with precision</p>
  </div>
  <div class="abs area-card" style="left:493px">
    <h3>Property Cleanup</h3>
    <div class="dash"></div>
    <p>Quick hauls, debris removal, or full cleanouts—no job too big or small</p>
  </div>
  <div class="abs area-card" style="left:908px">
    <h3>Ground Preparation</h3>
    <div class="dash" style="margin-bottom:2px"></div>
    <p>Pad preparation, brush removal, and fire lines—making proper-ties safe, functional, and project-ready</p>
  </div>

  <!-- ask banner -->
  <div class="abs rule" style="left:8px;top:1093px;width:1297px"></div>
  <div class="abs slant-banner" style="left:126px;top:1050px;width:600px;height:58px;font-size:36px;line-height:58px">Don’t See? Just Ask!</div>

  <!-- why choose us -->
  <h2 class="abs section-title why-title">Why Choose Us?</h2>

  <div class="abs perk-icon" style="left:139px;top:1230px">
    <svg width="46" height="50" viewBox="0 0 46 50" fill="none" stroke="#0d0d0d" stroke-width="2.5"><circle cx="23" cy="30" r="17"/><path d="M23 3c-5 0-8 3-8 7 0 5 8 11 8 11s8-6 8-11c0-4-3-7-8-7z"/><circle cx="23" cy="10" r="2.5"/><rect x="14" y="29" width="18" height="10"/><path d="M12 29h22l-3-5H15z"/></svg>
  </div>
  <div class="abs perk-icon" style="left:378px;top:1230px">
    <svg width="50" height="50" viewBox="0 0 50 50" fill="none" stroke="#0d0d0d" stroke-width="2.5"><circle cx="25" cy="25" r="22"/><circle cx="25" cy="25" r="13"/><path d="M19 25l4 4 8-9"/></svg>
  </div>
  <div class="abs perk-label" style="left:48px;top:1313px">Locally owned<br>since 2022</div>
  <div class="abs perk-label" style="left:288px;top:1313px">Licensed and<br>Insured</div>

  <div class="abs perk-icon" style="left:139px;top:1392px">
    <svg width="50" height="46" viewBox="0 0 50 46" fill="none" stroke="#0d0d0d" stroke-width="2.5"><circle cx="25" cy="13" r="10"/><path d="M25 7v12M28 9.5h-4.5a2 2 0 000 4h3a2 2 0 010 4H22"/><path d="M4 36l10-8h10l6 4h-9M4 42l12-4 20-8 8 2-22 12H10"/></svg>
  </div>
  <div class="abs perk-icon" style="left:378px;top:1392px">
    <svg width="46" height="50" viewBox="0 0 46 50" fill="none" stroke="#0d0d0d" stroke-width="2.5"><circle cx="23" cy="19" r="15"/><path d="M23 10l3 6 6 1-4.5 4 1 6-5.5-3-5.5 3 1-6L14 17l6-1z"/><path d="M13 31l-6 14 7-3 4 6 5-13M33 31l6 14-7-3-4 6-5-13"/></svg>
  </div>
  <div class="abs perk-label" style="left:46px;top:1479px">Reliable &amp;<br>Affordable</div>
  <div class="abs perk-note" style="left:41px;top:1543px">No corners cut, Professional results you can trust</div>
  <div class="abs perk-label" style="left:288px;top:1484px">Quality work</div>
  <div class="abs perk-note wide" style="left:283px;top:1526px">on time / references<br>/ flexible / follow-up.</div>

  <!-- call banner -->
  <div class="abs rule" style="left:0;top:1671px;width:600px"></div>
  <div class="abs slant-banner" style="left:21px;top:1628px;width:600px;height:57px;font-size:40px;line-height:57px">Call or Text Today!</div>

  <div class="abs contact" style="top:1710px">
    <span class="contact-icon"><svg width="20" height="20" viewBox="0 0 20 20" fill="none" stroke="#fff" stroke-width="1.6"><circle cx="10" cy="10" r="8"/><ellipse cx="10" cy="10" rx="3.5" ry="8"/><path d="M2 10h16M3.5 5.5h13M3.5 14.5h13"/></svg></span>
    <span class="contact-text">www.brackleyyard.example</span>
  </div>
  <div class="abs contact" style="top:1762px">
    <span class="contact-icon"><svg width="20" height="16" viewBox="0 0 20 16" fill="none" stroke="#fff" stroke-width="1.6"><rect x="1" y="1" width="18" height="14" rx="1.5"/><path d="M1 2l9 7 9-7"/></svg></span>
    <span class="contact-text">sales@brackleyyard.example</span>
  </div>
  <div class="abs contact" style="top:1806px">
    <span class="contact-icon"><svg width="20" height="20" viewBox="0 0 20 20" fill="#fff"><path d="M5 2l3 4-2 2c1 2.5 3.5 5 6 6l2-2 4 3-2 3C9 18 2 11 2 4z"/></svg></span>
    <span class="contact-text phone">(555) 019-4827</span>
  </div>

  <!-- what we do -->
  <div class="abs panel-back"></div>
  <div class="abs panel"></div>
  <div class="abs panel-outline"></div>
  <h2 class="abs section-title panel-title">What We Do</h2>

  <div class="abs col-head" style="left:747px;top:1326px">Remove</div>
  <div class="abs dot-rule" style="left:656px;top:1370px;width:220px"></div>
  <div class="abs col-head" style="left:1016px;top:1330px;width:238px;text-align:right">Install</div>
  <div class="abs dot-rule" style="left:1016px;top:1373px;width:238px"></div>

  <div class="abs task" style="left:745px;top:1407px"><span class="task-icon"><svg width="16" height="18" viewBox="0 0 16 18" fill="none" stroke="#fff" stroke-width="1.5"><path d="M1 4h14M5 4V2h6v2M3 4l1 13h8l1-13M6.5 7v7M9.5 7v7"/></svg></span>Junk Removal</div>
  <div class="abs task" style="left:745px;top:1452px"><span class="task-icon"><svg width="16" height="18" viewBox="0 0 16 18" fill="none" stroke="#fff" stroke-width="1.5"><rect x="2" y="4" width="12" height="13" rx="1"/><path d="M5 1h6v3M5 8v6M8 8v6M11 8v6"/></svg></span>Trash &amp; Waste Hauling</div>
  <div class="abs task" style="left:745px;top:1498px"><span class="task-icon"><svg width="18" height="18" viewBox="0 0 18 18" fill="none" stroke="#fff" stroke-width="1.5"><path d="M2 8h11l-2 6H4zM13 8l3-4"/><circle cx="5" cy="16" r="1.3"/><path d="M6 5c1-3 4-3 5-1"/></svg></span>Yard and Garden Cleaning</div>
  <div class="abs task" style="left:745px;top:1544px"><span class="task-icon"><svg width="16" height="18" viewBox="0 0 16 18" fill="none" stroke="#fff" stroke-width="1.5"><rect x="2" y="1" width="10" height="16" rx="1"/><path d="M2 6h10M9 10l5 5M14 10l-5 5"/></svg></span>Appliance Removal</div>

  <div class="abs task" style="left:1136px;top:1403px"><span class="task-icon"><svg width="18" height="18" viewBox="0 0 18 18" fill="none" stroke="#fff" stroke-width="1.5"><path d="M9 10V4M9 7c-3 0-4-2-4-4 3 0 4 2 4 4zM9 6c0-2 1-4 4-4 0 2-1 4-4 4z"/><circle cx="4" cy="14" r="1.5"/><circle cx="9" cy="15" r="1.5"/><circle cx="14" cy="14" r="1.5"/></svg></span>Mulch</div>
  <div class="abs task" style="left:1136px;top:1448px"><span class="task-icon"><svg width="18" height="16" viewBox="0 0 18 16" fill="none" stroke="#fff" stroke-width="1.5"><rect x="2" y="4" width="14" height="10" rx="1"/><path d="M5 8h8M5 11h5M6 4V1h6v3"/></svg></span>D.G.</div>
  <div class="abs task" style="left:1136px;top:1494px"><span class="task-icon"><svg width="16" height="18" viewBox="0 0 16 18" fill="none" stroke="#fff" stroke-width="1.5"><path d="M3 10h10l-1.5 7h-7zM8 10V5M8 6c-2 0-4-1-4-4 3 0 4 2 4 4zM8 5c0-2 1-4 4-4 0 3-2 4-4 4z"/></svg></span>Plants</div>
  <div class="abs task" style="left:1136px;top:1540px"><span class="task-icon"><svg width="18" height="16" viewBox="0 0 18 16" fill="#fff"><path d="M1 15l3-6 4-2 3 3 2-1 4 6z"/><circle cx="14" cy="4" r="1.3"/><circle cx="11" cy="3" r="1"/></svg></span>Rock</div>

  <div class="abs col-head" style="left:731px;top:1625px;text-transform:uppercase">Maintenance &amp; Other</div>
  <div class="abs dot-rule" style="left:656px;top:1670px;width:412px"></div>

  <div class="abs task" style="left:730px;top:1683px"><span class="task-icon"><svg width="18" height="18" viewBox="0 0 18 18" fill="none" stroke="#fff" stroke-width="1.5"><circle cx="8" cy="3" r="1.8"/><path d="M8 5l-1 6 3 5M7 11l-3 5M7 7l4 2 3-3M15 4v13"/></svg></span>Yard clean up</div>
  <div class="abs task" style="left:730px;top:1728px;align-items:flex-start"><span class="task-icon"><svg width="18" height="18" viewBox="0 0 18 18" fill="none" stroke="#fff" stroke-width="1.5"><path d="M3 16c3-6 5-8 9-9M7 12c-3-1-4-4-3-7 3 1 4 3 3 7z"/><circle cx="14" cy="4" r="2"/></svg></span><span>Weed prevention<br>(pre-emergent)</span></div>
  <div class="abs task" style="left:996px;top:1683px"><span class="task-icon"><svg width="18" height="16" viewBox="0 0 18 16" fill="none" stroke="#fff" stroke-width="1.5"><path d="M1 7l8-5 8 5M3 9h12v3H3zM11 10h3"/></svg></span>Roof &amp; gutter cleaning</div>
  <div class="abs task" style="left:996px;top:1728px"><span class="task-icon"><svg width="18" height="18" viewBox="0 0 18 18" fill="none" stroke="#fff" stroke-width="1.5"><path d="M3 16V4l1.5-2L6 4v12M8 16V4l1.5-2L11 4v12M13 16V4l1.5-2L16 4v12M1 7h17M1 13h17"/></svg></span>Fence &amp; deck staining</div>

</div>
</div>
</body>
</html>
```